KWT Contracting services . Building and maintenance services, optic fibre installation

Business cards and logo design.I need a logo that I can use on business cards ,workwear and on my vehicles. I would like the KWT to be the main or larger text and contracting services to be the smaller or less important text.I like monograms, modern designs and repeating patterns symbols. I am also a Gemini and my favourite number is 22 so if this can be any inspiration to help with the design. Am thinking of the using German flag colours as a his is my family’s heritage. And the other 2 main colours I wear is black and white.But any ideas are appreciated.I do not need a design that is trade specific but a design that could be used for any business.

Target Market(s)

General public

Contact Information for Business Card

KWT Contracting Services ( front of business card)

(Back of business card)
Milo Brackwood
0471539264
Maintenance services
Optic fibre and data installation

Logo Text

Logo can just be pattern or monogram or incorporate KWT . I like the gemini star sign and the number 22

Colors
ec1f27
000000
fbee3e
ffffff

Requirements
Must have
• Logo and KWT Contracting Services on the front of business card
Nice to have
• Possible use of German flag colours.
• Modern design.
• Design to be able to be used on black or white background as I want to put it on clothing

```html
<!DOCTYPE html>
<html lang="en">
<head>
<meta charset="utf-8">
<title>KWT Contracting Services – Business Cards</title>
<link rel="stylesheet" href="https://fonts.googleapis.com/css2?family=Exo+2:wght@400;500;600;700&display=swap">
<style>
  :root {
    --red: #ec1f27;
    --yellow: #fbee3e;
    --orange: #f47a22;
    --black: #000000;
    --card-black: #141414;
    --white: #ffffff;
    --grey-text: #2a2a2a;
    --stage: #1a1a1a;
  }
  * { box-sizing: border-box; margin: 0; padding: 0; }
  html, body {
    width: 1200px; height: 900px; overflow: hidden;
    background: var(--stage);
    font-family: "Exo 2", sans-serif;
  }
  .canvas {
    position: relative; width: 1200px; height: 900px;
    display: flex; align-items: center; justify-content: center; gap: 48px;
  }
  .card {
    position: relative; width: 530px; height: 303px;
    border-radius: 4px; overflow: hidden;
    box-shadow: 0 18px 40px rgba(0,0,0,.55);
  }

  /* Front */
  .card--front { background: var(--white); display: flex; align-items: center; justify-content: center; }
  .brand { display: flex; flex-direction: column; align-items: flex-start; }
  .brand__row { display: flex; align-items: center; gap: 14px; }
  .brand__square { width: 22px; height: 22px; background: var(--red); }
  .brand__name {
    font-weight: 700; font-size: 96px; line-height: .9; letter-spacing: 4px;
    color: var(--red);
  }
  .brand__tagline {
    margin-top: 8px; font-weight: 600; font-size: 17px; letter-spacing: 2px;
    color: var(--grey-text); text-transform: uppercase;
  }

  /* Back */
  .card--back { background: var(--card-black); }
  .card__texture {
    position: absolute; inset: 0;
    background: radial-gradient(ellipse at 30% 40%, #1f1f1f 0%, #0d0d0d 100%);
  }
  .card__band {
    position: absolute; top: 0; right: 0; width: 150px; height: 100%;
    background: linear-gradient(200deg, var(--yellow) 0%, var(--orange) 18%, var(--red) 40%, var(--red) 100%);
    display: flex; align-items: center; justify-content: center;
  }
  .card__band-name {
    transform: rotate(-90deg);
    font-weight: 500; font-size: 118px; letter-spacing: 6px;
    color: #1b1b1b; white-space: nowrap;
  }
  .details {
    position: absolute; left: 34px; top: 26px; width: 330px;
  }
  .details__brand { display: flex; align-items: center; gap: 10px; }
  .details__square { width: 14px; height: 14px; background: var(--red); }
  .details__brand-name {
    font-weight: 700; font-size: 52px; line-height: .9; letter-spacing: 3px; color: var(--red);
  }
  .details__tagline {
    margin-top: 4px; font-weight: 600; font-size: 11px; letter-spacing: 1.6px;
    color: var(--white); text-transform: uppercase;
  }
  .details__person {
    margin-top: 16px; font-weight: 600; font-size: 20px; letter-spacing: 1.5px;
    color: var(--white); text-transform: uppercase;
  }
  .contact { list-style: none; margin-top: 6px; }
  .contact__item { display: flex; align-items: center; gap: 8px; color: var(--red); }
  .contact__item--phone { font-size: 18px; font-weight: 500; letter-spacing: 1px; }
  .contact__item--email { font-size: 12.5px; margin-top: 3px; }
  .contact__icon {
    width: 13px; height: 13px; background: var(--red); border-radius: 2px;
    display: flex; align-items: center; justify-content: center; flex: none;
  }
  .details__rule { height: 1px; background: var(--red); margin: 8px 0 12px; width: 300px; }
  .services { list-style: none; }
  .services__item {
    display: flex; align-items: center; gap: 8px;
    font-size: 11.5px; font-weight: 500; letter-spacing: 1px;
    color: var(--white); text-transform: uppercase; line-height: 1.6;
  }
  .services__bullet { width: 7px; height: 7px; background: var(--red); flex: none; }
</style>
</head>
<body>
<main class="canvas">

  <section class="card card--front" aria-label="Business card front">
    <div class="brand">
      <div class="brand__row">
        <span class="brand__square"></span>
        <span class="brand__name">KWT</span>
      </div>
      <span class="brand__tagline">Contracting Services</span>
    </div>
  </section>

  <section class="card card--back" aria-label="Business card back">
    <div class="card__texture" role="img" aria-label="Dark textured card background"></div>

    <div class="details">
      <div class="details__brand">
        <span class="details__square"></span>
        <span class="details__brand-name">KWT</span>
      </div>
      <p class="details__tagline">Contracting Services</p>
      <p class="details__person">Milo Brackwood</p>
      <ul class="contact">
        <li class="contact__item contact__item--phone">
          <span class="contact__icon">
            <svg width="9" height="9" viewBox="0 0 24 24"><path fill="#fff" d="M6.6 10.8a15.1 15.1 0 0 0 6.6 6.6l2.2-2.2a1 1 0 0 1 1-.25 11.4 11.4 0 0 0 3.6.57 1 1 0 0 1 1 1V20a1 1 0 0 1-1 1A17 17 0 0 1 3 4a1 1 0 0 1 1-1h3.5a1 1 0 0 1 1 1c0 1.25.2 2.45.57 3.57a1 1 0 0 1-.25 1z"/></svg>
          </span>
          0471-539-264
        </li>
        <li class="contact__item contact__item--email">
          <span class="contact__icon">
            <svg width="9" height="9" viewBox="0 0 24 24"><path fill="none" stroke="#fff" stroke-width="2.5" d="M3 6h18v12H3zM3 6l9 7 9-7"/></svg>
          </span>
          kwtcontracting22@mailbox.net
        </li>
      </ul>
      <div class="details__rule"></div>
      <ul class="services">
        <li class="services__item"><span class="services__bullet"></span>Fibre Optic and Data</li>
        <li class="services__item"><span class="services__bullet"></span>Maintenance Services</li>
      </ul>
    </div>

    <div class="card__band">
      <span class="card__band-name">KWT</span>
    </div>
  </section>

</main>
</body>
</html>
```